Vinto PR Website

Vinto PR are a PR company with a requirement for a new website. In consultation with the client, we have defined a wireframe for a homepage to show content and functionality. A PDF of the wire frame is attached.
Current site http://www.vinto-pr.co.uk/
Updates
If you are using Stock Photography - please use PixVault
Dear All
Unfortunately, my client didn't like any of the designs submitted.
I've uploaded 3 examples of the type of photography that will appear in the carousel as supplied by the client.
Target Market(s)
Business to Business/Professionals - high value clients
Number of Pages Required
1 page
Requirements
Must have
- Colour scheme is attached as a .ase file from Kuler and can be viewed on Kuler if you search for 'VINTO PR Palette'
Corporate Typeface is Futura Book - use of Cufon is OK
Current Logo to be reatainedCall 2 Action Buttons will be controlled via the CMS so a generic background may be useful for these.
Nice to have
- RSS feeds

```html
<!DOCTYPE html>
<html lang="en">
<head>
<meta charset="utf-8">
<title>Vinto PR – Home</title>
<link rel="stylesheet" href="https://fonts.googleapis.com/css2?family=Jost:wght@400;500&display=swap">
<style>
:root{
  --teal-dark:#0b5d6f;
  --teal:#13788c;
  --teal-mid:#56b0a6;
  --teal-light:#9ed6d0;
  --aqua:#a8f0ea;
  --ink:#0d6275;
  --body:#4a4a4a;
  --card:#f4f4f4;
  --rule:#c8c8c8;
}
*{box-sizing:border-box;margin:0;padding:0}
html,body{width:953px;height:1200px;overflow:hidden;background:#fff}
body{position:relative;font-family:Verdana,"DejaVu Sans",sans-serif;color:var(--body)}
.abs{position:absolute}
.futura{font-family:"Jost",sans-serif;font-weight:400}

/* header */
.brand{left:76px;top:18px;font-size:36px;letter-spacing:5px;color:var(--ink)}
.social{left:614px;width:272px;top:22px;font-size:9.5px;font-weight:bold;color:var(--ink);display:flex;justify-content:space-between;align-items:center}
.social .net{font-family:"Jost",sans-serif;font-weight:500;font-size:14px;color:var(--teal)}
.callus{right:65px;top:47px;font-size:21px;color:var(--ink)}

/* nav */
.nav{left:0;top:80px;width:953px;height:44px;background:linear-gradient(#1b8aa0,#0b6278);border-top:2px solid #0a4f5e}
.nav ul{list-style:none;display:flex;justify-content:space-between;position:absolute;left:109px;width:776px;top:0;height:42px;align-items:center;font-family:"Jost",sans-serif;font-size:14px;color:#fff}
.nav li{white-space:nowrap}
.nav li.sep{opacity:.9}
.nav li.active{background:#333;height:42px;line-height:42px;padding:0 15px;position:relative}
.nav li.active::after{content:"";position:absolute;left:50%;bottom:-8px;margin-left:-8px;border:8px solid transparent;border-top-color:#333;border-bottom:0}

/* hero */
.hero{left:0;top:124px;width:953px;height:222px;background:linear-gradient(135deg,#a9dcd6,#92cfc8 60%,#a4d9d3)}
.topics{left:74px;top:16px;list-style:none;font-family:"Jost",sans-serif;font-size:21px;color:var(--ink)}
.topics li{height:40px;line-height:40px;padding-left:6px}
.topics li.current{color:#fff;position:relative;width:229px;height:31px;line-height:30px;margin-bottom:9px}
.topics li.current svg{position:absolute;left:0;top:0;z-index:0}
.topics li.current span{position:relative}
.feature{left:361px;top:11px;width:528px;height:204px;background:linear-gradient(#fff,#e9e9e9);border:1px solid #d5d5d5}
.feature h2{position:absolute;left:17px;top:7px;font-size:26px;color:var(--ink)}
.feature p{position:absolute;left:19px;width:335px;font-size:10.4px;line-height:15px;color:var(--ink)}
.feature .more{position:absolute;left:19px;top:181px;font-size:10.5px;font-weight:bold;color:var(--ink);text-decoration:underline}
.portrait{position:absolute;left:362px;top:9px;width:145px;height:182px;border:2px solid #fff;background:linear-gradient(#f2f2f2,#d9c7b4 55%,#2a2a2a)}

/* welcome */
.welcome{left:79px;top:375px;width:502px}
.welcome h1{font-size:30px;color:var(--ink);margin-bottom:20px}
.welcome p{font-size:10.4px;line-height:12px;margin-bottom:12px}
.vrule{border-left:1px dotted #b5b5b5}

/* news boxes */
.box{width:231px;height:290px;background:linear-gradient(#fafafa,#eaeaea);border:1px solid var(--rule);font-size:10px;line-height:12px;color:#3a3a3a}
.box .tag{position:absolute;left:-3px;top:9px;height:31px}
.box .tag span{position:absolute;left:8px;top:0;line-height:31px;font-family:"Jost",sans-serif;font-size:21px;color:#fff;white-space:nowrap}
.box .txt{position:absolute;left:16px;right:12px}
.box .dots{border-top:1px dotted #777;margin:8px 0}
.box .more{position:absolute;right:12px;bottom:12px;font-size:10.5px;font-weight:bold;color:var(--ink);text-decoration:underline}
.thumb{float:right;width:66px;height:68px;margin:-12px 0 4px 4px;background:linear-gradient(#e6e6e6,#c9b39a 60%,#555)}

/* call to action */
.c2a{left:633px;width:279px;height:97px;border:3px solid var(--teal-mid);background:linear-gradient(#5aaea6,#8ccbc3 57%,#bfe4df 58%,#c8e9e4)}
.c2a span{position:absolute;left:7px;bottom:2px;font-family:"Jost",sans-serif;font-size:25px;color:var(--ink)}
.chev{left:762px}

/* footer */
.footer{left:0;top:988px;width:953px;height:181px;background:linear-gradient(#98d7d1,#a8f0ea)}
.fcol h3{font-family:"Jost",sans-serif;font-weight:400;font-size:17px;color:var(--ink);border-bottom:1px solid var(--ink);width:195px;line-height:20px}
.fcol ul{list-style:none;font-size:9.5px;font-weight:bold;letter-spacing:.6px;color:var(--ink)}
.fcol li{height:20px;line-height:20px}
.signup h3{font-family:"Jost",sans-serif;font-weight:500;font-size:19px;color:var(--ink)}
.signup p{font-size:9px;line-height:11px;letter-spacing:.5px;color:var(--ink);width:195px}
.field{left:0;top:72px;width:190px;height:28px;background:#fff;border:1px solid var(--ink);font-size:10px;font-weight:bold;color:var(--ink);padding:7px 0 0 7px;letter-spacing:.5px}
.subscribe{left:0;top:111px;width:86px;height:20px;border-radius:3px;background:linear-gradient(#1d8ea4,#0b5f73);color:#fff;font-family:"Jost",sans-serif;font-size:15px;text-align:center;line-height:20px}
.bottom{left:0;top:1169px;width:953px;height:31px;background:linear-gradient(#1b8aa0,#0b6278);color:#fff;font-size:9.6px;font-weight:bold;letter-spacing:.5px;line-height:31px}
</style>
</head>
<body>

<!-- header -->
<div class="abs brand futura">Vinto PR</div>
<div class="abs social"><span>Email Us:</span><span class="net">Parlivox</span><span class="net">Quillnest</span><span class="net">Kinmeld</span></div>
<div class="abs callus futura">Call us now 0141 555 0199</div>

<nav class="abs nav">
  <ul>
    <li class="active">Home</li>
    <li>Vinto Services</li><li class="sep">|</li>
    <li>Press Office</li><li class="sep">|</li>
    <li>Vinto Case Studies</li><li class="sep">|</li>
    <li>Vinto People</li><li class="sep">|</li>
    <li>Blog</li><li class="sep">|</li>
    <li>Vinto News</li><li class="sep">|</li>
    <li>Contact Us</li>
  </ul>
</nav>

<!-- hero -->
<section class="abs hero">
  <ul class="abs topics">
    <li class="current">
      <svg width="229" height="31" viewBox="0 0 229 31"><polygon points="0,0 210,0 229,15.5 210,31 0,31" fill="#0d6275" stroke="#0a4a58" stroke-width="2"/></svg>
      <span>Online Public Relations</span>
    </li>
    <li>Media Relations</li>
    <li>Consumer Campaigns</li>
    <li>Crisis Public Relations</li>
    <li>Internal Communications</li>
  </ul>
  <article class="abs feature">
    <h2 class="futura">Online Public Relations</h2>
    <p style="top:50px">Lorem Ipsum is simply dummy text of the printing and typesetting industry. Lorem Ipsum has been the industry's standard dummy text ever since the 1500s.</p>
    <p style="top:110px">When an unknown printer took a galley of type and scrambled it to make a type specimen book. It has survived not only five centuries, but also the leap into electronic typesetting, remaining essentially unchanged.</p>
    <span class="more">View More</span>
    <div class="portrait" role="img" aria-label="Portrait photo of a smiling businesswoman"></div>
  </article>
</section>

<!-- welcome -->
<section class="abs welcome">
  <h1 class="futura">Welcome to Vinto PR</h1>
  <p>Vinto Public Relations is one of Scotland’s leading independent agencies. Founded in 2000, we were determined to create a public relations service with a real difference – hence the name.</p>
  <p>Vinto Public Relation’s trademark is a fresh, creative and hard working approach to public relations. It is an approach that secures real results for our clients.</p>
  <p>We are an agency with intelligence, integrity and imagination offering a comprehensive, results driven public relations service covering traditional and online public relations strategy and support.</p>
  <p>Lorem Ipsum is simply dummy text of the printing and typesetting industry. Lorem Ipsum has been the industry's standard dummy text ever since the 1500s.</p>
</section>

<div class="abs vrule" style="left:604px;top:383px;height:587px"></div>
<div class="abs vrule" style="left:327px;top:645px;height:325px"></div>

<!-- client news -->
<article class="abs box" style="left:75px;top:656px">
  <div class="tag"><svg width="148" height="31" viewBox="0 0 148 31"><polygon points="0,0 132,0 148,15.5 132,31 0,31" fill="#0d6275" stroke="#0a4a58" stroke-width="2"/></svg><span>Client News</span></div>
  <div class="txt" style="top:55px">
    Phasellus sapien ipsum, interdum ut dapibus in, hendrerit nec nulla. Donec<br><br>
    egestas scelerisque metus, nec placeratlectus ultrices ac. Nam sodales<br>mollis euismod. Mauris ornare viverra dignissim.
    <div class="dots" style="margin:14px 0 16px"></div>
    egestas scelerisque metus, nec placeratlectus ultrices ac. Nam sodales<br>mollis euismod. Mauris ornare viverra dignissim.
  </div>
  <span class="more">More</span>
</article>

<!-- blog -->
<article class="abs box" style="left:352px;top:656px">
  <div class="tag"><svg width="200" height="31" viewBox="0 0 200 31"><polygon points="0,0 184,0 200,15.5 184,31 0,31" fill="#0d6275" stroke="#0a4a58" stroke-width="2"/></svg><span>Latest Blog Entries</span></div>
  <div class="txt" style="top:67px">
    <div class="thumb" role="img" aria-label="Photo of a man wearing glasses"></div>
    Phasellus sapien ipsum, interdum ut dapibus in, hendrerit nec nulla Donec.<br><br>
    egestas scelerisque metus, nec placeratlectus ultrices ac. Nam sodales<br>mollis euismod. Mauris ornare viverra dignissim.
    <div class="dots" style="margin:6px 0 4px"></div>
    egestas scelerisque metus, nec placeratlectus ultrices ac. Nam sodales<br>mollis euismod. Mauris ornare viverra dignissim.
  </div>
  <span class="more">More</span>
</article>

<!-- call to action -->
<svg class="abs chev" style="top:388px" width="20" height="26" viewBox="0 0 20 26"><path d="M1 2l9 8 9-8M1 12l9 8 9-8" fill="none" stroke="#666" stroke-width="4"/></svg>
<div class="abs c2a" style="top:417px"><span>C2A Buttons</span></div>
<svg class="abs chev" style="top:529px" width="20" height="26" viewBox="0 0 20 26"><path d="M1 2l9 8 9-8M1 12l9 8 9-8" fill="none" stroke="#666" stroke-width="4"/></svg>
<div class="abs c2a" style="top:558px"><span>C2A Buttons</span></div>
<svg class="abs chev" style="top:675px" width="20" height="26" viewBox="0 0 20 26"><path d="M1 2l9 8 9-8M1 12l9 8 9-8" fill="none" stroke="#666" stroke-width="4"/></svg>
<div class="abs c2a" style="top:704px"><span>C2A Buttons</span></div>
<svg class="abs chev" style="top:819px" width="20" height="26" viewBox="0 0 20 26"><path d="M1 2l9 8 9-8M1 12l9 8 9-8" fill="none" stroke="#666" stroke-width="4"/></svg>
<div class="abs c2a" style="top:848px"><span>C2A Buttons</span></div>

<!-- footer -->
<footer class="abs footer">
  <div class="abs fcol" style="left:88px;top:37px">
    <h3>Services</h3>
    <ul><li>Online Public Relations</li><li>Media Relations</li><li>Consumer Campaigns</li><li>Crisis Public Relations</li><li>Internal Communications</li></ul>
  </div>
  <div class="abs fcol" style="left:322px;top:37px">
    <h3 style="width:185px">Links</h3>
    <ul style="padding-left:2px"><li>Subscribe to RSS Feed</li><li>Our Kinmeld page</li><li>Link Three</li><li>Link Four</li></ul>
  </div>
  <div class="abs signup" style="left:679px;top:37px">
    <h3>E-News Sign-up</h3>
    <p>Subscribe to our Newsletter to recieve news about Our Services, Products and Events.</p>
    <div class="abs field">Email Address</div>
    <div class="abs subscribe">Subscribe</div>
  </div>
</footer>
<div class="abs bottom">
  <span class="abs" style="left:76px">© Copyright Notice | Site Credit | Legal</span>
  <span class="abs" style="right:77px;white-space:nowrap">Home &nbsp;|&nbsp; About Us &nbsp;|&nbsp; Services &nbsp;|&nbsp; Blog &nbsp;|&nbsp; Contact Us</span>
</div>

</body>
</html>
```